The Harbor Parking Lot Vision Flags

Size: 3 banners - 2' x 4' banners (portrait)
Design: all the same design with different text
text on banner 1: Building Solid Lives
text on banner 2: Come. Hear. Do. Luke 6
text on banner 3: Worship Center
Details: Use the colors red, white and black and use the h logo attached
Make white the main color (not too much black and not too much red) Keep design simple - not a lot of different textures - more "quince like"

Target Market(s)

30-50 year olds

Industry/Entity Type

Parking

Font styles to use
Sans Serif

Colors
ec1f27
fbfbfb
1b1b1b

Requirements
Must have
• Logo and the colors red white and black
Nice to have
• simple - clean - cool
Should not have
• busy backgrounds and textures

```html
<!DOCTYPE html>
<html lang="en">
<head>
<meta charset="utf-8">
<title>The Lantern Parking Lot Vision Flags</title>
<link rel="stylesheet" href="https://fonts.googleapis.com/css2?family=Exo+2:wght@300;700&display=swap">
<style>
  :root {
    --red: #ec1f27;
    --white: #fbfbfb;
    --black: #1b1b1b;
    --stage: #9b9b9b;
  }
  * { margin: 0; padding: 0; box-sizing: border-box; }
  html, body { width: 1200px; height: 1000px; overflow: hidden; }
  body {
    background: var(--stage);
    font-family: "Exo 2", "Helvetica Neue", Arial, sans-serif;
    position: relative;
  }
  .flag {
    position: absolute;
    width: 363px;
    height: 727px;
    background: var(--white);
    overflow: hidden;
  }
  .flag--one { left: 26px; top: 30px; }
  .flag--two { left: 422px; top: 118px; }
  .flag--three { left: 810px; top: 237px; }
  .flag__bands { position: absolute; inset: 0; width: 100%; height: 100%; }
  .brand {
    position: absolute;
    left: 100px; right: 10px; top: 95px;
    display: flex; align-items: center; justify-content: center; gap: 10px;
    color: var(--red);
    font-weight: 700;
    font-size: 34px;
    white-space: nowrap;
  }
  .brand__dot {
    width: 22px; height: 22px; border-radius: 50%;
    background: var(--red);
  }
  .tagline {
    position: absolute;
    left: 92px; right: 0;
    text-align: center;
    color: var(--black);
    font-size: 68px;
    font-weight: 300;
    letter-spacing: -1px;
  }
  .tagline strong { font-weight: 700; }
  .tagline span { display: block; }
  .flag--one .tagline { top: 271px; line-height: 92px; }
  .flag--two .tagline { top: 257px; line-height: 78px; }
  .flag--three .tagline { top: 301px; line-height: 95px; }
</style>
</head>
<body>
  <svg width="0" height="0" style="position:absolute">
    <defs>
      <g id="flag-bands">
        <path fill="var(--black)" d="M0 0 H14 V598 Q14 640 52 652 L300 727 H0 Z"/>
        <path fill="var(--white)" d="M0 650 L0 668 L180 727 L232 727 Z"/>
        <path fill="var(--white)" d="M0 692 L0 706 L60 727 L100 727 Z"/>
        <path fill="var(--red)" d="M36 0 H90 V592 Q90 606 104 610 L363 688 V727 L300 727 L70 654 Q36 642 36 605 Z"/>
      </g>
    </defs>
  </svg>

  <section class="flag flag--one">
    <svg class="flag__bands" viewBox="0 0 363 727" aria-hidden="true"><use href="#flag-bands"/></svg>
    <div class="brand"><span class="brand__dot"></span>The Lantern</div>
    <p class="tagline"><span>Building</span><strong><span>Solid</span></strong><span>Lives</span></p>
  </section>

  <section class="flag flag--two">
    <svg class="flag__bands" viewBox="0 0 363 727" aria-hidden="true"><use href="#flag-bands"/></svg>
    <div class="brand"><span class="brand__dot"></span>The Lantern</div>
    <p class="tagline"><span>Come.</span><span>Hear.</span><strong><span>Do.</span></strong><span>Luke 6</span></p>
  </section>

  <section class="flag flag--three">
    <svg class="flag__bands" viewBox="0 0 363 727" aria-hidden="true"><use href="#flag-bands"/></svg>
    <div class="brand"><span class="brand__dot"></span>The Lantern</div>
    <p class="tagline"><span>Worship</span><strong><span>Center</span></strong></p>
  </section>
</body>
</html>
```